Wellness company needs a label design for a new health product

The name of the product is Verdel Chews and is part of Corvina Well. It allows a person to alkalize and maintain a healthy pH so their body can be at optimal health. This is a new product that will be sold in health professional offices only so it should look professional but have a cutting edge appeal. We are open to color options, keeping in mind we want to look fresh not like everyone else out there. We have the existing logo for Corvina Well already designed that will be needed to be incorporated into the label design. To get the Corvina Well logo either go to www.corvwell.example or I have attached a few files. Please contact me if you need me to send logo. Label will wrap around a bottle which will need to have room for a list of ingredients as well as suggested use.

I added a few examples of lables, the first being too basic, I would like more than that. The next two are examples of lables with added design to give it some interest but keeping it still professional. We are looking for a professional feel with an interesting edge.

A thought might be to have a muted design or soft watermark effect in the background. Thanks for all ideas
Updates

We are happy to inform you that we have guaranteed this project. Look forward to seeing your designs.

Reason: We are extending this projesct because we have guaranteed this project. Look forward to working with you.

Reason: Have not received many designs so we are extending the project. Will update more specific details hope this will help. Appreciate your help, thanks

I added two more labels that we like to give an idea what we are looking for, hope this helps.  Have not received many designs look forward to more, thanks

I added some new ideas, I look forward to seeing more designers ideas.

Reason: Waiting for some changes and possible new designs to make our decision.

Target Market(s)

Health Care profesionals, Chiropractors, Wellness Centers

Industry/Entity Type

Health

Requirements
Must have
• Corvina Well logo
product name: Verdel Chews
Should not have
• No people or animals

```html
<!DOCTYPE html>
<html lang="en">
<head>
<meta charset="utf-8">
<title>Verdel Chews – Label</title>
<link href="https://fonts.googleapis.com/css2?family=Open+Sans:ital,wght@0,400;0,600;0,700;1,300;1,400;1,700;1,800&display=swap" rel="stylesheet">
<style>
  :root {
    --page: #ffffff;
    --green-deep: #5f9526;
    --green-mid: #8cb82a;
    --yellow-glow: #e9e21c;
    --purple: #5b2a8c;
    --purple-light: #7a44ad;
    --white: #ffffff;
    --logo-ink: #3a3a3a;
    --logo-panel-top: #fbfbfb;
    --logo-panel-bottom: #cfcfcf;
    --leaf: #4faa2a;
    --skin-tone: #c9a27e;
  }
  * { box-sizing: border-box; margin: 0; padding: 0; }
  html, body { width: 1200px; height: 528px; overflow: hidden; background: var(--page); }
  body { font-family: "Open Sans", Arial, sans-serif; }

  .label {
    position: absolute; left: 24px; top: 24px; width: 1152px; height: 480px;
    border-radius: 14px; overflow: hidden;
    background: radial-gradient(ellipse 46% 70% at 50% 45%, var(--yellow-glow) 0%, var(--green-mid) 60%, var(--green-deep) 100%);
  }

  .info-column { position: absolute; top: 40px; color: var(--white); font-style: italic; }
  .info-column h2 { font-size: 18.5px; font-weight: 800; letter-spacing: -0.2px; margin-bottom: 10px; }
  .info-column p { font-size: 10.4px; line-height: 13.35px; text-align: justify; }
  .info-column p + p { text-indent: 6px; }
  .ingredients { left: 28px; width: 160px; }
  .suggested-use { left: 964px; width: 156px; }

  .visual { position: absolute; }
  .leaves-left { left: 190px; top: 100px; width: 210px; height: 215px; border-radius: 50%;
    background: radial-gradient(circle, rgba(79,170,42,.85) 0%, rgba(79,170,42,.3) 65%, transparent 72%); }
  .leaves-right { left: 740px; top: 310px; width: 170px; height: 130px; border-radius: 50%;
    background: radial-gradient(circle, rgba(79,170,42,.85) 0%, rgba(79,170,42,.3) 65%, transparent 72%); }
  .figure-left { left: 250px; top: 30px; width: 250px; height: 420px; border-radius: 40% 40% 30% 30%;
    background: radial-gradient(ellipse at 50% 45%, rgba(40,40,40,.55) 0%, rgba(201,162,126,.35) 55%, transparent 72%); }
  .figure-right { left: 690px; top: 22px; width: 200px; height: 440px; border-radius: 40% 40% 30% 30%;
    background: radial-gradient(ellipse at 50% 50%, rgba(235,235,235,.8) 0%, rgba(201,162,126,.4) 55%, transparent 72%); }

  .brand-panel {
    position: absolute; left: 431px; top: 32px; width: 288px; height: 112px;
    border-radius: 10px; border: 2px solid #e8e8e8;
    background: linear-gradient(var(--logo-panel-top), var(--logo-panel-bottom));
    box-shadow: 0 2px 6px rgba(0,0,0,.25);
    display: flex; align-items: center; justify-content: center;
  }
  .brand-name { font-size: 34px; font-weight: 700; color: var(--logo-ink); letter-spacing: -0.5px; }

  .product-name {
    position: absolute; left: 376px; top: 170px; width: 400px; text-align: center;
    font-style: italic; font-weight: 800; font-size: 50px; line-height: 48px;
    color: var(--purple); letter-spacing: -1px; text-transform: uppercase;
  }

  .claim { position: absolute; left: 376px; top: 304px; width: 400px; text-align: center;
    color: var(--white); font-style: italic; text-transform: uppercase; }
  .claim span { display: block; }
  .claim .light { font-weight: 300; font-size: 34px; line-height: 40px; }
  .claim .bold { font-weight: 700; font-size: 21px; line-height: 26px; }
  .claim strong { font-weight: 800; }
</style>
</head>
<body>
<main class="label">
  <section class="info-column ingredients">
    <h2>INGREDIENTS</h2>
    <p>Lorem ipsum dolor sit amet, consectetur adipiscing elit. Suspendisse condimentum enim vel diam rhoncus rhoncus. Nunc porttitor blandit placerat. Proin tempus iaculis varius. Duis faucibus, lacus eu tincidunt lobortis, justo neque rutrum dui, nec semper quam tortor non leo. Nunc sodales porta erat vel ullamcorper. Aliquam pulvinar sem in leo pretium et pellentesque risus iaculis. Suspendisse potenti. Curabitur id est vitae leo placerat elementum. Nunc vestibulum pellentesque orci, et bibendum felis facilisis sed. Nullam scelerisque bibendum quam, a condimentum risus aliquam a. Ut imperdiet nisi et elit tincidunt ultricies. Cras ut ante ante. Etiam eget lorem lectus, ut ullamcorper leo. Curabitur lacinia, orci vitae mattis condimentum, nibh magna lobortis ligula, ut convallis odio lorem sed erat. Nulla tempus pharetra eros sit amet ullamcorper.</p>
  </section>

  <div class="visual leaves-left" role="img" aria-label="Green leaves illustration"></div>
  <div class="visual figure-left" role="img" aria-label="Photo of a leaping dancer in black"></div>
  <div class="visual leaves-right" role="img" aria-label="Green leaves illustration"></div>
  <div class="visual figure-right" role="img" aria-label="Photo of a woman with raised arms standing on a scale"></div>

  <div class="brand-panel"><span class="brand-name">Corvina Well</span></div>

  <h1 class="product-name">Verdel<br>Chews</h1>

  <p class="claim">
    <span class="light">Alkalize</span>
    <span class="bold">&amp; Maintain</span>
    <span class="light">a healthy <strong>pH</strong></span>
  </p>

  <section class="info-column suggested-use">
    <h2>SUGGESTED USE</h2>
    <p>Nam a ligula quis felis ornare lobortis. Ut eget eleifend massa. Morbi pharetra nisl non diam consequat et blandit turpis aliquam. Mauris ornare sagittis consectetur. Nullam ligula est, malesuada sed sagittis sit amet, interdum a sem. Donec aliquam eleifend diam quis dictum. Morbi at quam nulla, non aliquet ipsum. Maecenas ligula ante, varius vitae tempus eu, dictum et est. Etiam mattis, tortor a vulputate aliquam, orci enim hendrerit metus, vel dapibus tellus erat sit amet ipsum. Praesent non orci quis diam adipiscing tempus. Nunc ultricies dictum lorem, quis vulputate nisi placerat in. Suspendisse semper tincidunt libero. Nam eleifend egestas suscipit. Suspendisse eu elit orci, at accumsan ligula.Duis eu turpis sapien.</p>
    <p>Aliquam scelerisque neque ut orci feugiat varius bibendum magna venenatis. Maecenas sit amet mauris odio, eget lobortis nulla. Vivamus dignissim</p>
  </section>
</main>
</body>
</html>
```